Veltrix App's Dashboard Redesign

We are redesigning our existing Veltrix app (http://www.lunatrak.com) to use Veltrix's new Facet Design guidelines (read more here: http://www.plexora.com/design/).

We would like to see new designs of the app's main screen (see lunatrak_dashboard.png) from you.

The new dashboard screen design should:
A. follow Veltrix's new Facet Design guidelines
B. contain an actionbar at the top (with an icon for hints and a "hamburger menu icon" on the left)
C. contain 4 buttons to the app's other screens: 1. Edit today's symptoms, 2. Calendar view, 3. Timeline view, 4. Chart view. (Please, do not put the buttons into tabs, as we want to avoid putting tabs on other screens too)
D. keep the basic concept of the cycle wheel (circle/donut representing the days of cycle; distinguish passed/upcoming days of cycle; show current cycle day; show menses days/fertile days/ovulation day)
E. contain iconic or textual predictions of the number of days to the next menses/ovulation
F. be easily themable to different colors (as the app supports more color themes)

To get a better idea about the app in general and the dashboard/cycle wheel in particular, please install the app and read Petal Orbit Notes. This will help you understand the functional requirements.

Wheel

```html
<!DOCTYPE html>
<html lang="en">
<head>
<meta charset="utf-8">
<title>Veltrix Cycle Dashboard</title>
<link rel="stylesheet" href="https://fonts.googleapis.com/css2?family=Roboto:wght@300;400;500&display=swap">
<style>
  :root {
    --page-bg: #cfcfcf;
    --screen-bg: #fafafa;
    --status-bar: #c2185b;
    --app-bar: #ec407a;
    --nav-bar: #000000;
    --ring-base: #ff80ab;
    --ring-fertile: #b388ff;
    --ring-ovulation: #7c4dff;
    --ring-menses: #ec407a;
    --accent: #7c4dff;
    --text-main: #424242;
    --text-menu: #424242;
    --icon-grey: #616161;
    --dot-idle: #bdbdbd;
    --white: #ffffff;
  }
  * { margin: 0; padding: 0; box-sizing: border-box; }
  html, body { width: 694px; height: 1200px; overflow: hidden; background: var(--page-bg); }
  body { font-family: 'Roboto', Arial, sans-serif; }
  .board {
    position: relative; width: 756px; height: 1307px;
    transform: scale(0.918); transform-origin: 0 0;
  }
  .screen {
    position: absolute; width: 360px; height: 640px;
    background: var(--screen-bg); overflow: hidden;
  }
  .screen--a { left: 10px; top: 10px; }
  .screen--b { left: 386px; top: 10px; }
  .screen--c { left: 10px; top: 657px; }
  .screen--d { left: 386px; top: 657px; }
  .status-bar {
    height: 24px; background: var(--status-bar); color: var(--white);
    display: flex; justify-content: flex-end; align-items: center;
    gap: 6px; padding-right: 8px; font-size: 13px;
  }
  .app-bar {
    height: 56px; background: var(--app-bar); color: var(--white);
    display: flex; align-items: center; padding: 0 16px; position: relative;
  }
  .app-bar__title { margin-left: 34px; font-size: 19px; font-weight: 500; display: flex; align-items: center; gap: 6px; }
  .app-bar__hint { margin-left: auto; }
  .wheel-art { position: absolute; left: 0; top: 80px; }
  .nav-bar {
    position: absolute; left: 0; bottom: 0; width: 360px; height: 48px;
    background: var(--nav-bar); display: flex; justify-content: space-around; align-items: center; padding: 0 60px;
  }
  .fab {
    position: absolute; left: 288px; top: 520px; width: 56px; height: 56px; border-radius: 50%;
    background: var(--app-bar); display: flex; align-items: center; justify-content: center;
    box-shadow: 0 3px 6px rgba(0,0,0,.25);
  }
  .view-menu {
    position: absolute; left: 56px; top: 32px; width: 168px; padding: 8px 0;
    background: var(--white); box-shadow: 0 2px 8px rgba(0,0,0,.3); border-radius: 2px; z-index: 2;
  }
  .view-menu__item { height: 48px; display: flex; align-items: center; padding-left: 16px; gap: 18px; font-size: 16px; color: var(--text-menu); }
  .view-menu__item--active { color: var(--accent); }
  .ring-label { font-size: 24px; font-weight: 300; fill: var(--text-main); }
  .ring-label__num { font-weight: 500; }
  .bubble-text { font-size: 24px; font-weight: 300; fill: var(--white); }
  .bubble-text__num { font-weight: 400; }
  .pin-text { font-size: 25px; font-weight: 300; fill: var(--white); }
</style>
</head>
<body>
<div class="board">

  <!-- Screen: countdown pin -->
  <section class="screen screen--a">
    <div class="status-bar">
      <svg width="16" height="14" viewBox="0 0 16 14"><path d="M0 3 Q8 -3 16 3 L8 13Z" fill="#fff"/></svg>
      <svg width="14" height="14" viewBox="0 0 14 14"><path d="M14 0V14H0Z" fill="#fff"/></svg>
      <svg width="9" height="15" viewBox="0 0 9 15"><rect x="0" y="2" width="9" height="13" fill="#fff"/><rect x="3" y="0" width="3" height="2" fill="#fff"/></svg>
      <span>12:30</span>
    </div>
    <header class="app-bar">
      <svg width="18" height="12" viewBox="0 0 18 12"><path d="M0 1h18M0 6h18M0 11h18" stroke="#fff" stroke-width="2"/></svg>
      <span class="app-bar__title">Fertile phase <svg width="10" height="5"><path d="M0 0h10L5 5Z" fill="#fff"/></svg></span>
      <svg class="app-bar__hint" width="22" height="24" viewBox="0 0 22 24"><circle cx="11" cy="12" r="6" fill="#fff"/><rect x="8" y="17" width="6" height="4" fill="#fff"/><path d="M11 0v3M1 4l2 2M21 4l-2 2M0 12h3M19 12h3" stroke="#fff" stroke-width="1.6"/></svg>
    </header>
    <svg class="wheel-art" width="360" height="512" viewBox="0 80 360 512">
      <circle cx="180" cy="352" r="106" fill="none" stroke="var(--ring-base)" stroke-width="36"/>
      <path d="M74.4 361.2 A106 106 0 0 1 271.8 299" fill="none" stroke="var(--ring-fertile)" stroke-width="36"/>
      <path d="M127 260.2 A106 106 0 0 1 261.2 283.8" fill="none" stroke="var(--ring-ovulation)" stroke-width="44" stroke-linecap="round"/>
      <path d="M135.2 448 A106 106 0 0 1 80.4 388.3" fill="none" stroke="var(--ring-menses)" stroke-width="44" stroke-linecap="round"/>
      <g fill="#fff"><circle cx="202" cy="245" r="3.5"/><circle cx="212" cy="245" r="3.5"/><circle cx="202" cy="255" r="3.5"/><circle cx="212" cy="255" r="3.5"/><circle cx="207" cy="250" r="3"/></g>
      <path d="M74 331 L77 340 L86 343 L77 346 L74 355 L71 346 L62 343 L71 340Z" fill="#fff"/>
      <path d="M135 438 C140 446 142 450 142 453 A7 7 0 0 1 128 453 C128 450 130 446 135 438Z" fill="#fff"/>
      <g class="countdown-pin">
        <circle cx="180" cy="166" r="29" fill="var(--accent)"/>
        <path d="M157 183 L180 206 L203 183Z" fill="var(--accent)"/>
        <text class="pin-text" x="180" y="175" text-anchor="middle">14</text>
      </g>
      <path d="M129 341 C134 348 136 352 136 355 A7 7 0 0 1 122 355 C122 352 124 348 129 341Z" fill="var(--accent)"/>
      <text class="ring-label" x="154" y="360"><tspan class="ring-label__num">17</tspan> days</text>
      <circle cx="168" cy="428" r="3" fill="var(--app-bar)"/><circle cx="180" cy="428" r="3" fill="var(--dot-idle)"/><circle cx="192" cy="428" r="3" fill="var(--dot-idle)"/>
    </svg>
    <div class="fab"><svg width="20" height="20" viewBox="0 0 20 20"><path d="M2 18l1-5L14 2l4 4L7 17Z" fill="#fff"/></svg></div>
    <nav class="nav-bar">
      <svg width="16" height="16"><path d="M14 1L2 8l12 7Z" fill="none" stroke="#fff" stroke-width="1.8"/></svg>
      <svg width="18" height="18"><circle cx="9" cy="9" r="7" fill="none" stroke="#fff" stroke-width="1.8"/></svg>
      <svg width="16" height="16"><rect x="1" y="1" width="14" height="14" fill="none" stroke="#fff" stroke-width="1.8"/></svg>
    </nav>
  </section>

  <!-- Screen: view menu open -->
  <section class="screen screen--b">
    <div class="status-bar">
      <svg width="16" height="14" viewBox="0 0 16 14"><path d="M0 3 Q8 -3 16 3 L8 13Z" fill="#fff"/></svg>
      <svg width="14" height="14" viewBox="0 0 14 14"><path d="M14 0V14H0Z" fill="#fff"/></svg>
      <svg width="9" height="15" viewBox="0 0 9 15"><rect x="0" y="2" width="9" height="13" fill="#fff"/><rect x="3" y="0" width="3" height="2" fill="#fff"/></svg>
      <span>12:30</span>
    </div>
    <header class="app-bar">
      <svg width="18" height="12" viewBox="0 0 18 12"><path d="M0 1h18M0 6h18M0 11h18" stroke="#fff" stroke-width="2"/></svg>
      <svg class="app-bar__hint" width="22" height="24" viewBox="0 0 22 24"><circle cx="11" cy="12" r="6" fill="#fff"/><rect x="8" y="17" width="6" height="4" fill="#fff"/><path d="M11 0v3M1 4l2 2M21 4l-2 2M0 12h3M19 12h3" stroke="#fff" stroke-width="1.6"/></svg>
    </header>
    <div class="view-menu">
      <div class="view-menu__item view-menu__item--active"><svg width="22" height="22" viewBox="0 0 22 22"><circle cx="11" cy="11" r="8" fill="none" stroke="var(--accent)" stroke-width="4" stroke-dasharray="10 3"/></svg>Wheel</div>
      <div class="view-menu__item"><svg width="22" height="22" viewBox="0 0 22 22"><rect x="2" y="4" width="18" height="16" rx="2" fill="none" stroke="var(--icon-grey)" stroke-width="2"/><rect x="2" y="4" width="18" height="4" fill="var(--icon-grey)"/><rect x="12" y="13" width="4" height="4" fill="var(--icon-grey)"/></svg>Calendar</div>
      <div class="view-menu__item"><svg width="22" height="22" viewBox="0 0 22 22"><path d="M2 2v18h18" fill="none" stroke="var(--icon-grey)" stroke-width="2"/><path d="M4 16l5-6 4 3 6-8" fill="none" stroke="var(--icon-grey)" stroke-width="2"/></svg>Chart</div>
      <div class="view-menu__item"><svg width="22" height="22" viewBox="0 0 22 22"><path d="M2 5h2M2 11h2M2 17h2M7 5h13M7 11h13M7 17h13" stroke="var(--icon-grey)" stroke-width="2"/></svg>Timeline</div>
    </div>
    <svg class="wheel-art" width="360" height="512" viewBox="0 80 360 512">
      <circle cx="180" cy="352" r="106" fill="none" stroke="var(--ring-base)" stroke-width="36"/>
      <path d="M74.4 361.2 A106 106 0 0 1 271.8 299" fill="none" stroke="var(--ring-fertile)" stroke-width="36"/>
      <path d="M127 260.2 A106 106 0 0 1 261.2 283.8" fill="none" stroke="var(--ring-ovulation)" stroke-width="44" stroke-linecap="round"/>
      <path d="M135.2 448 A106 106 0 0 1 80.4 388.3" fill="none" stroke="var(--ring-menses)" stroke-width="44" stroke-linecap="round"/>
      <g fill="#fff"><circle cx="202" cy="245" r="3.5"/><circle cx="212" cy="245" r="3.5"/><circle cx="202" cy="255" r="3.5"/><circle cx="212" cy="255" r="3.5"/><circle cx="207" cy="250" r="3"/></g>
      <path d="M74 331 L77 340 L86 343 L77 346 L74 355 L71 346 L62 343 L71 340Z" fill="#fff"/>
      <path d="M135 438 C140 446 142 450 142 453 A7 7 0 0 1 128 453 C128 450 130 446 135 438Z" fill="#fff"/>
      <path d="M129 341 C134 348 136 352 136 355 A7 7 0 0 1 122 355 C122 352 124 348 129 341Z" fill="var(--accent)"/>
      <text class="ring-label" x="154" y="360"><tspan class="ring-label__num">17</tspan> days</text>
      <circle cx="168" cy="428" r="3" fill="var(--app-bar)"/><circle cx="180" cy="428" r="3" fill="var(--dot-idle)"/><circle cx="192" cy="428" r="3" fill="var(--dot-idle)"/>
    </svg>
    <div class="fab"><svg width="20" height="20" viewBox="0 0 20 20"><path d="M2 18l1-5L14 2l4 4L7 17Z" fill="#fff"/></svg></div>
    <nav class="nav-bar">
      <svg width="16" height="16"><path d="M14 1L2 8l12 7Z" fill="none" stroke="#fff" stroke-width="1.8"/></svg>
      <svg width="18" height="18"><circle cx="9" cy="9" r="7" fill="none" stroke="#fff" stroke-width="1.8"/></svg>
      <svg width="16" height="16"><rect x="1" y="1" width="14" height="14" fill="none" stroke="#fff" stroke-width="1.8"/></svg>
    </nav>
  </section>

  <!-- Screen: pregnancy week bubble -->
  <section class="screen screen--c">
    <div class="status-bar">
      <svg width="16" height="14" viewBox="0 0 16 14"><path d="M0 3 Q8 -3 16 3 L8 13Z" fill="#fff"/></svg>
      <svg width="14" height="14" viewBox="0 0 14 14"><path d="M14 0V14H0Z" fill="#fff"/></svg>
      <svg width="9" height="15" viewBox="0 0 9 15"><rect x="0" y="2" width="9" height="13" fill="#fff"/><rect x="3" y="0" width="3" height="2" fill="#fff"/></svg>
      <span>12:30</span>
    </div>
    <header class="app-bar">
      <svg width="18" height="12" viewBox="0 0 18 12"><path d="M0 1h18M0 6h18M0 11h18" stroke="#fff" stroke-width="2"/></svg>
      <span class="app-bar__title">Fertile phase <svg width="10" height="5"><path d="M0 0h10L5 5Z" fill="#fff"/></svg></span>
      <svg class="app-bar__hint" width="22" height="24" viewBox="0 0 22 24"><circle cx="11" cy="12" r="6" fill="#fff"/><rect x="8" y="17" width="6" height="4" fill="#fff"/><path d="M11 0v3M1 4l2 2M21 4l-2 2M0 12h3M19 12h3" stroke="#fff" stroke-width="1.6"/></svg>
    </header>
    <svg class="wheel-art" width="360" height="512" viewBox="0 80 360 512">
      <circle cx="180" cy="352" r="106" fill="none" stroke="var(--ring-base)" stroke-width="36"/>
      <path d="M74.4 361.2 A106 106 0 0 1 271.8 299" fill="none" stroke="var(--ring-fertile)" stroke-width="36"/>
      <path d="M127 260.2 A106 106 0 0 1 261.2 283.8" fill="none" stroke="var(--ring-ovulation)" stroke-width="44" stroke-linecap="round"/>
      <path d="M135.2 448 A106 106 0 0 1 80.4 388.3" fill="none" stroke="var(--ring-menses)" stroke-width="44" stroke-linecap="round"/>
      <g fill="#fff"><circle cx="202" cy="245" r="3.5"/><circle cx="212" cy="245" r="3.5"/><circle cx="202" cy="255" r="3.5"/><circle cx="212" cy="255" r="3.5"/><circle cx="207" cy="250" r="3"/></g>
      <path d="M74 331 L77 340 L86 343 L77 346 L74 355 L71 346 L62 343 L71 340Z" fill="#fff"/>
      <path d="M135 438 C140 446 142 450 142 453 A7 7 0 0 1 128 453 C128 450 130 446 135 438Z" fill="#fff"/>
      <rect x="50" y="137" width="260" height="55" rx="27.5" fill="var(--accent)"/>
      <path d="M166 191 L180 205 L194 191Z" fill="var(--accent)"/>
      <text class="bubble-text" x="180" y="173" text-anchor="middle"><tspan class="bubble-text__num">10</tspan>th week &amp; <tspan class="bubble-text__num">3</tspan>rd day</text>
      <path d="M129 341 C134 348 136 352 136 355 A7 7 0 0 1 122 355 C122 352 124 348 129 341Z" fill="var(--accent)"/>
      <text class="ring-label" x="154" y="360"><tspan class="ring-label__num">17</tspan> days</text>
      <circle cx="168" cy="428" r="3" fill="var(--app-bar)"/><circle cx="180" cy="428" r="3" fill="var(--dot-idle)"/><circle cx="192" cy="428" r="3" fill="var(--dot-idle)"/>
    </svg>
    <div class="fab"><svg width="20" height="20" viewBox="0 0 20 20"><path d="M2 18l1-5L14 2l4 4L7 17Z" fill="#fff"/></svg></div>
    <nav class="nav-bar">
      <svg width="16" height="16"><path d="M14 1L2 8l12 7Z" fill="none" stroke="#fff" stroke-width="1.8"/></svg>
      <svg width="18" height="18"><circle cx="9" cy="9" r="7" fill="none" stroke="#fff" stroke-width="1.8"/></svg>
      <svg width="16" height="16"><rect x="1" y="1" width="14" height="14" fill="none" stroke="#fff" stroke-width="1.8"/></svg>
    </nav>
  </section>

  <!-- Screen: pregnancy wheel with day dots -->
  <section class="screen screen--d">
    <div class="status-bar">
      <svg width="16" height="14" viewBox="0 0 16 14"><path d="M0 3 Q8 -3 16 3 L8 13Z" fill="#fff"/></svg>
      <svg width="14" height="14" viewBox="0 0 14 14"><path d="M14 0V14H0Z" fill="#fff"/></svg>
      <svg width="9" height="15" viewBox="0 0 9 15"><rect x="0" y="2" width="9" height="13" fill="#fff"/><rect x="3" y="0" width="3" height="2" fill="#fff"/></svg>
      <span>12:30</span>
    </div>
    <header class="app-bar">
      <svg width="18" height="12" viewBox="0 0 18 12"><path d="M0 1h18M0 6h18M0 11h18" stroke="#fff" stroke-width="2"/></svg>
      <span class="app-bar__title">Fertile phase <svg width="10" height="5"><path d="M0 0h10L5 5Z" fill="#fff"/></svg></span>
      <svg class="app-bar__hint" width="22" height="24" viewBox="0 0 22 24"><circle cx="11" cy="12" r="6" fill="#fff"/><rect x="8" y="17" width="6" height="4" fill="#fff"/><path d="M11 0v3M1 4l2 2M21 4l-2 2M0 12h3M19 12h3" stroke="#fff" stroke-width="1.6"/></svg>
    </header>
    <svg class="wheel-art" width="360" height="512" viewBox="0 80 360 512">
      <circle cx="180" cy="352" r="106" fill="none" stroke="var(--ring-base)" stroke-width="36"/>
      <path d="M74.4 361.2 A106 106 0 0 1 271.8 299" fill="none" stroke="var(--ring-fertile)" stroke-width="36"/>
      <path d="M127 260.2 A106 106 0 0 1 261.2 283.8" fill="none" stroke="var(--ring-ovulation)" stroke-width="44" stroke-linecap="round"/>
      <path d="M135.2 448 A106 106 0 0 1 80.4 388.3" fill="none" stroke="var(--ring-menses)" stroke-width="44" stroke-linecap="round"/>
      <circle cx="180" cy="352" r="110" fill="none" stroke="#fff" stroke-opacity=".8" stroke-width="2.4" stroke-linecap="round" stroke-dasharray="0 14.4"/>
      <circle cx="200" cy="250" r="9" fill="none" stroke="#fff" stroke-width="2.5"/><circle cx="200" cy="250" r="3" fill="#fff"/>
      <path d="M62 341 h20 a10 10 0 0 1 -20 0Z M72 341 v-9 a9 9 0 0 1 10 9" fill="#fff"/><circle cx="66" cy="354" r="2.5" fill="#fff"/><circle cx="79" cy="354" r="2.5" fill="#fff"/>
      <path d="M135 438 C140 446 142 450 142 453 A7 7 0 0 1 128 453 C128 450 130 446 135 438Z" fill="#fff"/>
      <rect x="50" y="137" width="260" height="55" rx="27.5" fill="var(--accent)"/>
      <path d="M166 191 L180 205 L194 191Z" fill="var(--accent)"/>
      <text class="bubble-text" x="180" y="173" text-anchor="middle"><tspan class="bubble-text__num">10</tspan>th week &amp; <tspan class="bubble-text__num">3</tspan>rd day</text>
      <path d="M129 341 C134 348 136 352 136 355 A7 7 0 0 1 122 355 C122 352 124 348 129 341Z" fill="var(--accent)"/>
      <text class="ring-label" x="154" y="360"><tspan class="ring-label__num">17</tspan> days</text>
      <circle cx="168" cy="428" r="3" fill="var(--app-bar)"/><circle cx="180" cy="428" r="3" fill="var(--dot-idle)"/><circle cx="192" cy="428" r="3" fill="var(--dot-idle)"/>
    </svg>
    <div class="fab"><svg width="20" height="20" viewBox="0 0 20 20"><path d="M2 18l1-5L14 2l4 4L7 17Z" fill="#fff"/></svg></div>
    <nav class="nav-bar">
      <svg width="16" height="16"><path d="M14 1L2 8l12 7Z" fill="none" stroke="#fff" stroke-width="1.8"/></svg>
      <svg width="18" height="18"><circle cx="9" cy="9" r="7" fill="none" stroke="#fff" stroke-width="1.8"/></svg>
      <svg width="16" height="16"><rect x="1" y="1" width="14" height="14" fill="none" stroke="#fff" stroke-width="1.8"/></svg>
    </nav>
  </section>

</div>
</body>
</html>
```